UI design for Fast Food Restaurant Self-Order App

Background:
App purpose: for fast food restaurant customers to self order food/drink by choosing item image, and make payment by tapping the credit card on the card terminal.
Reference: https://www.brivolkiosks.example/product-overview/self-order-kiosks/
Attachment:
Wireframes. (wire frames provide general idea and the information to display, they are not a strict guideline for layout design.)
Tarrowby's Self ordering app.
Intro:
We have built a (for restaurant and cafe) Self Ordering and Payment app, similar to Tarrowby's self ordering software in most of their new restaurants. Our app will be placed in a Quorvane Deskline 10 OS touch screen Kiosk(screen size 4:3 or Portrait 16:9) within the restaurant/cafe premise.
Pages to be designed:
Page 1. Food Browsing Page. displays all food images(to be provided by cafes) by categories, and displays the Cart. This page will lead to Page 2 or Page 3.
'Cart' section should include:
'cart items/selected items', its quantity and price. like Tarrowbys' app.
When click on a Cart Item, we need to allow to change quantity or 'change Choice'. The UI handling these change requests with ease will be one deciding factor for us to choose your design.
Fact: up to 10 food categories, and 10 - 25 food items under each categories.
When click on one item image, it goes to Page 2.
Page 2. Item Detail/Description Page. Shows description of the food, and its available Choice(other food items or Special Request, up to 12) will also be displayed. 'Add item to cart' action(Button Name: ADD) will happen here and go back to Browsing Page 1.
e.g. Item 'Fried Rice' Page. the Choice could be 'Add Egg', 'Add Meat', 'No Chilli' etc.
Page 3. Order Review Page. No edit features allowed on this page, only two buttons: 'No' to go back to Browsing Page, or 'Yes' to proceed to Payment Page 4. Check Tarrowby's screen.
Page 4. Payment Page - Prompt user to Insert or Tap credit card on the credit card terminal. (Exact wording: PLEASE FOLLOW INSTRUCTIONS DISPLAYED ON CREDIT CARD TERMINAL BELOW)
Page 5. Payment status. Successful / Failed.
Our considerations to pick the winner:
1. In terms of design for this task, we look out for page layout, effects, fonts, button style and overall colour scheme. the design should present itself in a clean and modern look, with minimum clicking or scrolling. The app aims to help customers choose and pay for their items quickly.
2.we need to handle both 4:3(as shown in wire frames) and 16:9 screens(like Tarrowby's). there will be a lot more vertical space to utilise when it is in 16:9, resulting less scrolling than 4:3. tell us what you think.
All questions are welcome.
Winner has opportunity to work on a few more app UI. Cheers!
Industry/Entity Type
Fast Food Restaurant
Requirements
Must have
- Button colour differentiation - helps people know what to click next.
- best use of screen space. minimum click and scrolls.
Nice to have
- any personal touch.
Should not have
- unrelated design pattern, e.g. a cute animal or flower pattern in the layout.

```html
<!DOCTYPE html>
<html lang="en">
<head>
<meta charset="utf-8">
<title>Fast Food Restaurant — Self-Order Kiosk</title>
<link rel="stylesheet" href="https://fonts.googleapis.com/css2?family=Inter:wght@400;500;600;700;800&display=swap">
<style>
  :root {
    --orange: #ff9800;
    --orange-soft: rgba(255, 152, 0, 0.22);
    --ink: #2f2f2f;
    --order-red: #ff3b30;
    --cancel-red: #ff0a0a;
    --pay-green: #00e36b;
    --white: #ffffff;
    --scroll-track: #d9d9d9;
    --scroll-thumb: #555555;
  }
  * { box-sizing: border-box; margin: 0; padding: 0; }
  html, body { width: 1200px; height: 750px; overflow: hidden; background: var(--white); }
  body { position: relative; font-family: "Inter", Arial, sans-serif; color: var(--ink); }

  .brand { position: absolute; left: 30px; top: 30px; width: 140px; text-align: center; }
  .brand-dot { width: 44px; height: 44px; border-radius: 50%; background: var(--orange); margin: 0 auto 18px; }
  .brand-name { font-size: 13px; font-weight: 400; color: var(--ink); letter-spacing: -0.2px; }

  .category-nav { position: absolute; left: 8px; top: 191px; width: 212px; list-style: none; }
  .category { position: absolute; left: 29px; font-size: 22px; font-weight: 600; white-space: nowrap; }
  .category.is-active {
    left: 0; top: 0; width: 211px; height: 58px; padding-left: 29px; line-height: 58px;
    background: var(--white); color: var(--orange); border-radius: 10px;
    box-shadow: 0 8px 28px var(--orange-soft);
  }

  .page-title { position: absolute; left: 328px; top: 56px; font-size: 44px; font-weight: 700; letter-spacing: -1px; }

  .product { position: absolute; width: 200px; text-align: center; }
  .product-photo { width: 180px; margin: 0 auto; border-radius: 40%; }
  .product-price { position: absolute; top: 0; font-size: 18px; font-weight: 700; color: var(--orange); }
  .product-name { position: absolute; left: 0; width: 100%; font-size: 18px; font-weight: 600; }

  .scrollbar { position: absolute; left: 925px; top: 198px; width: 4px; height: 544px; background: var(--scroll-track); border-radius: 2px; }
  .scrollbar-thumb { width: 4px; height: 77px; background: var(--scroll-thumb); border-radius: 2px; }

  .order-panel { position: absolute; left: 951px; top: 48px; width: 260px; height: 387px; background: var(--order-red); border-radius: 14px; color: var(--white); }
  .order-title { position: absolute; left: 21px; top: 10px; font-size: 20px; font-weight: 700; letter-spacing: -0.3px; }
  .order-rule { position: absolute; left: 21px; width: 218px; height: 1px; background: rgba(255,255,255,0.6); }
  .order-item { position: absolute; left: 21px; width: 208px; }
  .order-item-line { display: flex; justify-content: space-between; font-size: 14px; font-weight: 400; letter-spacing: -0.3px; }
  .order-item-size { font-size: 10.5px; font-weight: 600; color: #9e1a12; margin-top: 5px; }
  .order-total { position: absolute; left: 21px; top: 347px; width: 218px; display: flex; justify-content: space-between; font-size: 15px; font-weight: 700; }

  .options-label { position: absolute; left: 953px; top: 466px; font-size: 18px; font-weight: 500; letter-spacing: -0.3px; }
  .btn { position: absolute; border: none; font-family: inherit; color: var(--white); font-weight: 700; border-radius: 10px; text-align: center; }
  .btn-size { width: 99px; height: 42px; background: var(--orange); font-size: 14px; }
  .btn-pay { left: 951px; top: 608px; width: 223px; height: 71px; background: var(--pay-green); font-size: 30px; letter-spacing: -0.5px; }
  .btn-cancel { left: 951px; top: 694px; width: 224px; height: 42px; background: var(--cancel-red); font-size: 14px; }
</style>
</head>
<body>

  <header class="brand">
    <div class="brand-dot"></div>
    <p class="brand-name">Fast Food Restaurant</p>
  </header>

  <ul class="category-nav">
    <li class="category is-active">Angel cakes</li>
    <li class="category" style="top:89px">Apple cakes</li>
    <li class="category" style="top:155px">Banana cakes</li>
    <li class="category" style="top:217px">Birthday cakes</li>
    <li class="category" style="top:283px">Financier</li>
  </ul>

  <h1 class="page-title">Angel cakes</h1>

  <section class="product-grid">
    <article class="product" style="left:280px;top:212px">
      <div class="product-photo" role="img" aria-label="Layered sponge cake with cream and strawberries" style="height:134px;margin-top:12px;background:radial-gradient(ellipse at center,#e6c8b0 0%,#c99877 45%,#f2e4da 70%,rgba(255,255,255,0) 75%)"></div>
      <span class="product-price" style="right:-1px">$120</span>
      <h2 class="product-name" style="top:159px">Cherry Decorater</h2>
    </article>
    <article class="product" style="left:478px;top:212px">
      <div class="product-photo" role="img" aria-label="Pink mousse cake on chocolate base with strawberries" style="height:134px;margin-top:12px;width:120px;background:radial-gradient(ellipse at center,#f3b9c6 0%,#d98a9c 35%,#4a2d22 60%,rgba(255,255,255,0) 72%)"></div>
      <span class="product-price" style="right:12px">$110</span>
      <h2 class="product-name" style="top:159px">Ribbon &amp; Choco</h2>
    </article>
    <article class="product" style="left:660px;top:212px">
      <div class="product-photo" role="img" aria-label="Glossy chocolate cake topped with orange slices" style="height:134px;margin-top:12px;background:radial-gradient(ellipse at center,#2b1a14 0%,#3a2318 45%,#8a5a3a 60%,rgba(255,255,255,0) 72%)"></div>
      <span class="product-price" style="right:13px">$90</span>
      <h2 class="product-name" style="top:159px">Orange Flavor</h2>
    </article>

    <article class="product" style="left:270px;top:484px">
      <div class="product-photo" role="img" aria-label="Pink frosted cupcake with a bow" style="height:150px;margin-top:8px;width:110px;background:radial-gradient(ellipse at center,#fbe3ee 0%,#f576c4 45%,#e8329d 60%,rgba(255,255,255,0) 74%)"></div>
      <span class="product-price" style="right:42px">$9</span>
      <h2 class="product-name" style="top:170px">Party Fiesta</h2>
    </article>
    <article class="product" style="left:452px;top:484px">
      <div class="product-photo" role="img" aria-label="Caramelised honey custard tart" style="height:140px;margin-top:12px;width:130px;background:radial-gradient(ellipse at center,#e9c38c 0%,#c98a45 40%,#a06a3a 60%,rgba(255,255,255,0) 74%)"></div>
      <span class="product-price" style="right:20px">$11</span>
      <h2 class="product-name" style="top:170px">Honey Bee</h2>
    </article>
    <article class="product" style="left:680px;top:484px">
      <div class="product-photo" role="img" aria-label="Chocolate-topped layered slice with yellow flowers" style="height:160px;margin-top:4px;background:radial-gradient(ellipse at center,#f6d94a 0%,#3a2218 35%,#efe2c6 58%,rgba(255,255,255,0) 74%)"></div>
      <span class="product-price" style="right:1px">$16</span>
      <h2 class="product-name" style="top:170px">Sunflower</h2>
    </article>
  </section>

  <div class="scrollbar"><div class="scrollbar-thumb"></div></div>

  <aside class="order-panel">
    <h2 class="order-title">Order Place</h2>
    <div class="order-rule" style="top:44px"></div>
    <div class="order-item" style="top:56px">
      <div class="order-item-line"><span>Cherry Decorater - 1x</span><span>$120</span></div>
      <div class="order-item-size">Small (3lbs)</div>
    </div>
    <div class="order-item" style="top:107px">
      <div class="order-item-line"><span>Ribbon &amp; Choco - 1x</span><span>$110</span></div>
      <div class="order-item-size">Large (9lbs)</div>
    </div>
    <div class="order-item" style="top:157px">
      <div class="order-item-line"><span>Honey Bee&nbsp; - 2x</span><span>$22</span></div>
      <div class="order-item-size">Small</div>
    </div>
    <div class="order-rule" style="top:328px"></div>
    <div class="order-total"><span>Total</span><span>$252</span></div>
  </aside>

  <h3 class="options-label">Order options</h3>
  <button class="btn btn-size" style="left:951px;top:501px">Small</button>
  <button class="btn btn-size" style="left:1074px;top:501px">Medium</button>
  <button class="btn btn-size" style="left:951px;top:554px">Large</button>
  <button class="btn btn-size" style="left:1074px;top:554px">X- Large</button>
  <button class="btn btn-pay">Pay Now</button>
  <button class="btn btn-cancel">Cancel Order</button>

</body>
</html>
```